Brochure for software platform

We need a clean and professional brochure (max 4 pages) for one of our products called "Jurnex.io", see https://jurnex-example.io/en. The product is a software platform to manage the application and selection process for grants, awards or similar challenges. Our company is called Larkmont Systems AG and we are based in Switzerland. The brochure should be in English but might be translated into German. The design should be based on the information provided on the website and in the presentation available on google drive (with logo,...). See
https://files.example-share.net/folders/8KpQ2vTz7LmW3xRd?share=link
Additional screenshots for mockups can be provided once closer to the final design. Design should be clean and professional.

Target Market(s)

Foundations, Investors, Accelerators, Award organisers

Font styles to use
Other font styles liked:
• Opens Sans Light

Colors
0492cd
34a6d7
85cae6
0255a3
3377b5

Requirements
Must have
• Use white (or bright) background. And the blue logo color for font titles. At least one mockup with a screenshot of the platform (see website). No must of customer logos but if it fits we can provide some (see as on website).

```html
<!DOCTYPE html>
<html lang="en">
<head>
<meta charset="utf-8">
<title>Jurnex brochure spreads</title>
<link rel="stylesheet" href="https://fonts.googleapis.com/css2?family=Open+Sans:ital,wght@0,300;0,400;0,600;1,300;1,400&display=swap">
<style>
  :root {
    --canvas: #eceef0;
    --page: #ffffff;
    --brand: #3a9ee4;
    --brand-deep: #0492cd;
    --ink: #4a4a4a;
    --ink-soft: #6b6b6b;
    --band: #e6e6e6;
    --ui-dark: #2f3236;
    --ui-line: #d7dadd;
  }
  * { box-sizing: border-box; margin: 0; padding: 0; }
  html, body { width: 1200px; height: 1000px; overflow: hidden; }
  body { background: var(--canvas); font-family: "Open Sans", Arial, sans-serif; font-weight: 300; color: var(--ink); position: relative; }

  .spread { position: absolute; left: 266px; width: 668px; height: 470px; overflow: hidden; box-shadow: 0 2px 8px rgba(0,0,0,.15); background: var(--page); }
  .spread--cover { top: 24px; }
  .spread--inside { top: 508px; }
  .spread__art { position: absolute; inset: 0; }
  .spread__fold { position: absolute; left: 332px; top: 0; width: 4px; height: 470px; background: linear-gradient(90deg, rgba(0,0,0,.08), rgba(0,0,0,0)); }

  /* cover */
  .contact { position: absolute; left: 0; top: 36px; width: 334px; text-align: center; color: #fff; font-size: 8.5px; line-height: 10.5px; }
  .contact__label { font-weight: 600; margin-top: 8px; }
  .contact__label:first-child { margin-top: 0; }
  .trusted { position: absolute; left: 0; top: 176px; width: 334px; text-align: center; color: #fff; font-size: 10.5px; }
  .partners { position: absolute; left: 68px; top: 206px; width: 200px; display: grid; grid-template-columns: repeat(3, 36px); justify-content: space-between; row-gap: 14px; }
  .partner-badge { width: 36px; height: 14px; background: rgba(255,255,255,.92); }
  .brand-lockup { position: absolute; left: 520px; top: 392px; display: flex; align-items: center; gap: 8px; }
  .brand-lockup__dot { width: 24px; height: 24px; border-radius: 50%; background: var(--brand); }
  .brand-lockup__name { font-size: 31px; font-weight: 400; color: var(--brand); letter-spacing: .5px; line-height: 1; }
  .brand-tagline { position: absolute; left: 492px; top: 430px; width: 160px; padding-top: 3px; border-top: 1px solid #b9b9b9; font-size: 11px; color: var(--ink); text-align: right; }

  /* inside left */
  .section-tab { position: absolute; left: 0; display: flex; align-items: center; font-size: 10.5px; font-weight: 600; text-transform: uppercase; }
  .section-tab--about { top: 22px; width: 170px; height: 16px; background: #fff; color: var(--brand); padding-left: 24px; }
  .section-tab--about::before { content: ""; position: absolute; left: 0; top: 0; width: 18px; height: 16px; background: var(--brand-deep); }
  .about { position: absolute; left: 24px; top: 48px; width: 294px; color: #fff; font-size: 8.4px; line-height: 10.6px; }
  .about p { margin-bottom: 9px; }
  .about__sub { font-weight: 400; }
  .section-tab--services { top: 262px; color: var(--brand); padding-left: 24px; }
  .section-tab--services::before { content: ""; position: absolute; left: 0; top: 1px; width: 18px; height: 10px; background: var(--brand); }
  .service { position: absolute; left: 26px; width: 300px; display: flex; gap: 22px; }
  .service__icon { width: 36px; height: 34px; flex: none; }
  .service__title { font-size: 9px; font-weight: 600; color: #333; text-transform: uppercase; margin-bottom: 1px; }
  .service__text { font-size: 8.4px; line-height: 10.4px; color: var(--ink); }

  /* inside right */
  .dam-title { position: absolute; left: 350px; top: 12px; font-size: 11.5px; font-weight: 600; color: #333; text-transform: uppercase; }
  .dam-sub { position: absolute; left: 350px; top: 27px; font-size: 8.5px; color: var(--ink-soft); }
  .step { position: absolute; top: 70px; width: 72px; font-size: 8.2px; line-height: 10px; color: var(--ink); }
  .step__name { font-style: italic; font-size: 9.5px; color: var(--brand); margin-bottom: 2px; }
  .ui-title { position: absolute; left: 348px; top: 158px; font-size: 11.5px; font-weight: 600; color: #333; text-transform: uppercase; }
  .feature { position: absolute; font-size: 7.8px; line-height: 9.2px; color: var(--ink); }
  .feature p { margin-bottom: 3px; }
  .feature__name { font-style: italic; font-size: 9.2px; line-height: 11px; color: var(--brand); margin-bottom: 2px; }
  .feature--right { text-align: right; }
</style>
</head>
<body>

<section class="spread spread--cover" aria-label="Brochure cover spread">
  <svg class="spread__art" width="668" height="470" viewBox="0 0 668 470">
    <defs>
      <linearGradient id="coverBlue" x1="0" y1="0" x2="1" y2="1">
        <stop offset="0" stop-color="#4d9fe6"/>
        <stop offset="1" stop-color="#7cbdf1"/>
      </linearGradient>
      <linearGradient id="coverWhite" x1="0" y1="1" x2="1" y2="0">
        <stop offset="0" stop-color="#ffffff"/>
        <stop offset="1" stop-color="#e6e8ea"/>
      </linearGradient>
      <linearGradient id="photoTone" x1="0" y1="0" x2="1" y2="1">
        <stop offset="0" stop-color="#c9ccd0"/>
        <stop offset=".45" stop-color="#eef0f2"/>
        <stop offset="1" stop-color="#d8dbde"/>
      </linearGradient>
    </defs>
    <rect x="0" y="0" width="334" height="470" fill="url(#coverBlue)"/>
    <polygon points="92,470 334,150 334,470" fill="url(#coverWhite)"/>
    <rect x="334" y="0" width="334" height="470" fill="#ffffff"/>
    <polygon points="334,0 386,0 334,70" fill="url(#coverBlue)"/>
    <g role="img" aria-label="Photo: people at a desk reviewing charts on paper and a laptop">
      <polygon points="398,0 668,0 668,318 556,470 334,470 334,86" fill="url(#photoTone)"/>
    </g>
    <polygon points="524,0 536,0 334,296 334,278" fill="#5aa8ea" opacity=".9"/>
  </svg>
  <div class="spread__fold"></div>

  <div class="contact">
    <div class="contact__label">ADDRESS</div>
    <div>Larkmont Systems AG</div>
    <div>Talweg 41</div>
    <div>8004 Zürich, Switzerland</div>
    <div class="contact__label">EMAIL</div>
    <div>mail@larkmont-example.ch</div>
    <div class="contact__label">REGISTRATION DETAILS</div>
    <div>UID: CHE-512.808.417</div>
    <div>VAT: CHE-512.808.417 MWST</div>
  </div>
  <div class="trusted">Trusted by leading programs and organisations</div>
  <div class="partners" aria-label="Partner organisations">
    <span class="partner-badge"></span><span class="partner-badge"></span><span class="partner-badge"></span>
    <span class="partner-badge"></span><span class="partner-badge"></span><span class="partner-badge"></span>
  </div>

  <div class="brand-lockup"><span class="brand-lockup__dot"></span><span class="brand-lockup__name">jurnex</span></div>
  <div class="brand-tagline">Digital application management</div>
</section>

<section class="spread spread--inside" aria-label="Brochure inside spread">
  <svg class="spread__art" width="668" height="470" viewBox="0 0 668 470">
    <defs>
      <linearGradient id="insideBlue" x1="0" y1="0" x2="1" y2="1">
        <stop offset="0" stop-color="#4f9fe6"/>
        <stop offset="1" stop-color="#78bbf0"/>
      </linearGradient>
      <linearGradient id="insidePage" x1="0" y1="0" x2="1" y2="0">
        <stop offset="0" stop-color="#ffffff"/>
        <stop offset="1" stop-color="#eceef0"/>
      </linearGradient>
    </defs>
    <rect x="0" y="0" width="334" height="470" fill="url(#insidePage)"/>
    <polygon points="0,0 334,0 334,150 0,252" fill="url(#insideBlue)"/>
    <polygon points="0,252 334,150 334,176 0,258" fill="#a9d3f4"/>
    <rect x="0" y="461" width="668" height="6" fill="#4fa1e8"/>

    <line x1="342" y1="58" x2="660" y2="58" stroke="#6fb4ea" stroke-width="1"/>
    <g fill="#fff" stroke="#6fb4ea" stroke-width="1">
      <circle cx="370" cy="58" r="4.5"/><circle cx="434" cy="58" r="4.5"/>
      <circle cx="510" cy="58" r="4.5"/><circle cx="585" cy="58" r="4.5"/>
    </g>

    <rect x="336" y="190" width="332" height="86" fill="var(--band)"/>
    <rect x="336" y="360" width="332" height="92" fill="var(--band)"/>

    <g>
      <rect x="342" y="196" width="112" height="74" fill="#fff" stroke="var(--ui-line)"/>
      <rect x="342" y="196" width="22" height="74" fill="var(--ui-dark)"/>
      <rect x="370" y="212" width="78" height="6" fill="#e4f1d9"/>
      <g fill="var(--ui-line)">
        <rect x="370" y="224" width="60" height="3"/><rect x="370" y="232" width="70" height="3"/>
        <rect x="370" y="240" width="50" height="3"/><rect x="370" y="248" width="64" height="3"/>
      </g>
    </g>
    <g>
      <rect x="550" y="282" width="112" height="74" fill="#fff" stroke="var(--ui-line)"/>
      <rect x="550" y="282" width="22" height="74" fill="var(--ui-dark)"/>
      <g fill="var(--ui-line)">
        <rect x="578" y="300" width="78" height="3"/><rect x="578" y="310" width="78" height="3"/>
        <rect x="578" y="320" width="78" height="3"/><rect x="578" y="330" width="78" height="3"/>
      </g>
      <g fill="#5aa8ea">
        <rect x="642" y="309" width="14" height="5"/><rect x="642" y="319" width="14" height="5"/><rect x="642" y="329" width="14" height="5"/>
      </g>
    </g>
    <g>
      <rect x="342" y="366" width="112" height="78" fill="#fff" stroke="var(--ui-line)"/>
      <rect x="342" y="366" width="22" height="78" fill="var(--ui-dark)"/>
      <g fill="var(--ui-line)"><rect x="370" y="378" width="36" height="20"/><rect x="410" y="378" width="38" height="20"/></g>
      <circle cx="384" cy="424" r="10" fill="#d6d8db"/>
      <path d="M384 424 L384 414 A10 10 0 0 1 393 428 Z" fill="#3a3d41"/>
      <circle cx="414" cy="424" r="10" fill="#d6d8db"/>
      <path d="M414 424 L414 414 A10 10 0 0 1 405 429 Z" fill="#3a3d41"/>
    </g>

    <g fill="none" stroke="#333" stroke-width="1.3">
      <rect x="30" y="356" width="24" height="28" rx="3"/>
      <line x1="36" y1="360" x2="36" y2="380"/><line x1="42" y1="360" x2="42" y2="380"/><line x1="48" y1="360" x2="48" y2="380"/>
      <rect x="34" y="368" width="4" height="4" fill="#fff"/><rect x="40" y="374" width="4" height="4" fill="#fff"/><rect x="46" y="364" width="4" height="4" fill="#fff"/>
      <path d="M28 424 h18 a4 4 0 0 1 4 4 v6 a4 4 0 0 1 -4 4 h-10 l-5 4 v-4 h-3 a4 4 0 0 1 -4 -4 v-6 a4 4 0 0 1 4 -4 z"/>
      <path d="M50 430 h4 a4 4 0 0 1 4 4 v5 a4 4 0 0 1 -4 4 h-1 v3 l-4 -3 h-6"/>
    </g>
    <rect x="32" y="294" width="22" height="30" rx="3" fill="#d9dbde" role="img" aria-label="Icon: strategy game piece"/>
  </svg>
  <div class="spread__fold"></div>

  <div class="section-tab section-tab--about">About us</div>
  <div class="about">
    <p>Jurnex is a product of Larkmont Systems AG.</p>
    <p class="about__sub">Company profile</p>
    <p>Larkmont Systems was founded in 2013 by Mara Tessin and Dr Lukas Brenner. The company's aim is to simplify business processes through digital solutions. Larkmont Systems' services include web and mobile application development, strategy and consulting.</p>
    <p>Our expertise includes software engineering, data analytics and project management. These skills combined with creative thinking enable us to implement enterprise solutions using cutting-edge technology and innovative approaches.</p>
  </div>

  <div class="section-tab section-tab--services">Our services</div>
  <div class="service" style="top:290px">
    <div class="service__icon"></div>
    <div><div class="service__title">Strategic consulting</div>
      <div class="service__text">We define workflow design and implementation<br>strategy based on your existing processes.</div></div>
  </div>
  <div class="service" style="top:356px">
    <div class="service__icon"></div>
    <div><div class="service__title">Platform customization</div>
      <div class="service__text">We brand, tailor and customize the platform based<br>on your specific requirements.</div></div>
  </div>
  <div class="service" style="top:416px">
    <div class="service__icon"></div>
    <div><div class="service__title">Ongoing support</div>
      <div class="service__text">We insure high quality products and user satisfaction<br>through ongoing support, development and maintenance.</div></div>
  </div>

  <div class="dam-title">Digital application management</div>
  <div class="dam-sub">Fully tailored to your process without Email and complex spreadsheets.</div>
  <div class="step" style="left:360px"><div class="step__name">Application</div>Applicants submit their data through a dedicated and custom branded web portal.</div>
  <div class="step" style="left:434px"><div class="step__name">Revision</div>Judges review applications on the portal through a tailored workflow and multi-step process.</div>
  <div class="step" style="left:508px"><div class="step__name">Selection</div>Applications can be easily selected based on quantitative scores and qualitative feedback.</div>
  <div class="step" style="left:585px"><div class="step__name">Feedback</div>The integrated messaging and feedback tools allow direct engagement with applicants.</div>

  <div class="ui-title">Intuitive management interface</div>
  <div class="feature" style="left:460px; top:193px; width:204px">
    <div class="feature__name">Structured Application</div>
    <p>Applications are accepted through a custom branded interface. Data is entered into web forms with different question or field types, including text, numeric, multichoice and media upload fields.</p>
    <p>If activated, applicants can use the integrated messaging functionality to communicate with organizers.</p>
  </div>
  <div class="feature feature--right" style="left:344px; top:280px; width:200px">
    <div class="feature__name">Tailored Workflow</div>
    <p>The revision and selection workflow can include multiple steps, judging rounds and assessment types.</p>
    <p>Internal and external jury members can assess all or selected applications and provide feedback through weighted assessment scores, yes/ no ratings, color scores and comments.</p>
  </div>
  <div class="feature" style="left:460px; top:363px; width:204px">
    <div class="feature__name">Live analytics and reporting</div>
    <p>Key data, including application status and selected fields, are instantly visualized on interactive and dynamic dashboards.</p>
    <p>Assessment and judging status can be visualized in real time.</p>
    <p>Applications can be tracked beyond selection, through integration with the portfolio management module.</p>
  </div>
</section>

</body>
</html>
```